Antigen Preservation Bureau

The company will provide a contract research services to stabilize various viruses, viral vectors, and vaccines. It may offer some licensing opportunities for stabilizing technologies. Main area of applications are pharmaceutical, therapeutic, and vaccination field. The company aspires to develop room temperature vaccines for global distribution beyond the current cold chain.

Target Market(s)

pharmaceutical, therapeutic and vaccination fields

Coding

Coded - Design and coding required

Number of Pages Required

4 page

Requirements
Must have
• Incorporate a APB logo, attached at the bottom, on the Web page

```html
<!DOCTYPE html>
<html lang="en">
<head>
<meta charset="utf-8">
<title>Antigen Preservation Bureau</title>
<link rel="stylesheet" href="https://fonts.googleapis.com/css2?family=Poppins:wght@300;400;500;600&display=swap">
<style>
:root{
  --navy:#1f2f6b;
  --blue:#0a9bd8;
  --blue-dark:#2f6db3;
  --ink:#333333;
  --muted:#555555;
  --hero:#f4f4f4;
  --band:#f1f1f1;
  --white:#ffffff;
  --footer:#333333;
  --video:#3a3a3a;
  --line:#e3e3e3;
}
*{box-sizing:border-box;margin:0;padding:0}
html,body{width:1200px;height:2416px;overflow:hidden}
body{position:relative;font-family:"Poppins",sans-serif;color:var(--ink);background:var(--white)}
.section{position:absolute;left:0;width:1200px}
a{color:inherit;text-decoration:none}

/* header */
.site-header{top:0;height:89px;background:var(--white);border-top:3px solid var(--blue)}
.brand{position:absolute;left:139px;top:32px;color:var(--navy);font-size:22px;line-height:26px;font-weight:400;white-space:nowrap}
.contact-pill{position:absolute;left:749px;top:0;width:322px;height:34px;background:var(--blue);border-radius:0 0 18px 18px;color:var(--white);font-size:15px;display:flex;align-items:center;justify-content:center;gap:22px}
.contact-pill span{display:flex;align-items:center;gap:7px}
.main-nav{position:absolute;left:569px;top:58px;display:flex;font-size:14px;color:var(--ink)}
.main-nav a{display:block}
.main-nav a:nth-child(1){width:90px;font-weight:500;color:var(--navy)}
.main-nav a:nth-child(2){width:108px}
.main-nav a:nth-child(3){width:103px}
.main-nav a:nth-child(4){width:93px;font-size:17px;margin-top:-2px}

/* hero */
.hero{top:89px;height:309px;background:var(--hero);display:flex;align-items:center;justify-content:center}
.hero p{width:920px;text-align:center;font-size:25px;line-height:37px;color:var(--ink);margin-top:-12px}

/* section heading */
.section-title{text-align:center;color:var(--navy);font-size:21px;font-weight:400}
.section-title::after{content:"";display:block;width:120px;height:2px;background:var(--blue);margin:7px auto 0}
.lead{text-align:center;font-size:13px;line-height:22px;color:var(--muted)}

/* applications */
.applications{top:398px;height:453px}
.applications .section-title{margin-top:57px}
.applications .lead{width:800px;margin:14px auto 0}
.app-cards{position:absolute;top:171px;left:137px;display:flex;gap:24px}
.app-card{width:290px;height:212px;background:var(--hero);box-shadow:0 0 10px rgba(0,0,0,.13);text-align:center;padding-top:26px}
.app-card svg{width:72px;height:72px}
.app-card h3{margin-top:18px;font-size:17px;font-weight:500;color:var(--blue)}
.app-card p{margin:4px auto 0;width:276px;font-size:12.5px;line-height:20px;color:var(--ink)}
.app-card.is-active{background:var(--blue);box-shadow:none}
.app-card.is-active h3,.app-card.is-active p{color:var(--white)}

/* about */
.about{top:851px;height:423px;background:var(--band)}
.about h2{position:absolute;left:144px;top:58px;font-size:22px;font-weight:400;color:var(--navy)}
.about h2::after{content:"";display:block;width:120px;height:2px;background:var(--navy);margin-top:3px}
.about-text{position:absolute;left:147px;top:103px;width:430px;font-size:12.5px;line-height:23px;color:var(--ink)}
.about-text p+p{margin-top:8px}
.btn{display:inline-flex;align-items:center;justify-content:center;color:var(--white);font-weight:500}
.btn-read{position:absolute;left:142px;top:311px;width:105px;height:30px;border-radius:15px;background:var(--blue-dark);font-size:12px}
.video{position:absolute;left:617px;top:95px;width:446px;height:246px;background:var(--video);color:#eaeaea}
.video-name{position:absolute;left:0;right:0;top:40px;text-align:center;font-size:20px;font-weight:400}
.video-play{position:absolute;left:198px;top:98px}

/* news */
.news{top:1274px;height:600px}
.news .section-title{margin-top:62px}
.news-cards{position:absolute;top:121px;left:139px;display:flex;gap:36px}
.news-card{width:282px;height:432px;border:1px solid var(--line);background:var(--white);text-align:center}
.news-media{position:relative;height:211px}
.news-card:nth-child(1) .news-media{background:linear-gradient(135deg,#1c5c8f,#6aa3c8 55%,#c9d6df)}
.news-card:nth-child(2) .news-media{background:linear-gradient(135deg,#d9dde2,#f4f5f6 50%,#6c7fae)}
.news-card:nth-child(3) .news-media{background:linear-gradient(135deg,#4a4a4a,#c4ccd3 50%,#e6eaee)}
.date{position:absolute;left:0;top:0;width:48px;height:52px;background:var(--navy);color:var(--white)}
.date b{display:block;font-size:23px;font-weight:400;line-height:32px}
.date i{display:block;font-style:normal;font-size:10px;background:var(--blue);line-height:20px}
.news-card h3{margin:18px auto 0;width:266px;font-size:15px;line-height:23px;font-weight:400;color:var(--ink)}
.news-card p{margin:14px auto 0;width:256px;font-size:12.5px;line-height:23px;color:var(--ink)}
.news-card .more{display:block;margin-top:13px;font-size:12px;font-style:italic;color:var(--navy)}

/* licensing */
.licensing{top:1874px;height:232px;text-align:center}
.licensing h2{margin-top:44px;font-size:23px;font-weight:400;color:var(--ink)}
.licensing .lead{width:740px;margin:12px auto 0;line-height:22px}
.btn-call{margin-top:12px;width:144px;height:37px;background:var(--blue);font-size:15px;font-weight:400;gap:7px}

/* footer */
.site-footer{top:2106px;height:264px;background:var(--footer);color:#e6e6e6}
.footer-col{position:absolute;top:44px}
.footer-col h4{font-size:14px;font-weight:400;color:var(--white)}
.footer-col h4::after{content:"";display:block;width:38px;height:2px;background:var(--white);margin-top:5px}
.links{left:139px}
.links ul{list-style:none;margin-top:15px;font-size:12.5px;line-height:25px}
.contacts{left:290px}
.contact-row{display:flex;gap:16px;font-size:12.5px;line-height:18px;margin-top:16px}
.contact-row svg{flex:none;margin-top:2px}
.map-col{left:535px}
.map{margin-top:15px;width:226px;height:145px;background:linear-gradient(135deg,#dfe3e6,#eef0f1 50%,#d8dde2)}
.follow{left:805px}
.socials{display:flex;gap:10px;margin-top:19px}
.socials span{width:26px;height:26px;border-radius:50%;background:var(--white)}
.footer-brand{margin-top:30px;font-size:18px;line-height:24px;font-weight:400;color:var(--white);white-space:nowrap}
.bottom-bar{top:2370px;height:46px;background:var(--blue);color:var(--white);font-size:11px}
.bottom-bar p{position:absolute;top:15px}
.copy{left:139px}
.legal{left:861px}
</style>
</head>
<body>

<header class="section site-header">
  <div class="brand">Antigen Preservation Bureau</div>
  <div class="contact-pill">
    <span><svg width="20" height="20" viewBox="0 0 24 24" fill="none" stroke="#fff" stroke-width="2"><circle cx="12" cy="12" r="10"/><path d="M8.5 7.5l2 2-1 1.5a7 7 0 003.5 3.5l1.5-1 2 2-1.5 1.5c-3.5 0-8-4.5-8-8z" fill="#fff" stroke="none"/></svg>123.456.7890</span>
    <span><svg width="20" height="16" viewBox="0 0 20 16" fill="none" stroke="#fff" stroke-width="1.8"><rect x="1" y="1" width="18" height="14"/><path d="M1 1l9 7 9-7"/></svg>inquiry@apb.com</span>
  </div>
  <nav class="main-nav">
    <a href="#">Home</a><a href="#">About Us</a><a href="#">Services</a><a href="#">News</a><a href="#">Contact Us</a>
  </nav>
</header>

<section class="section hero">
  <p>We are experts in formulation science and pharmaceutical process development with special emphasis on recombinant proteins, ADCs / cytotoxics and live virus vaccines.</p>
</section>

<section class="section applications">
  <h2 class="section-title">Our Main Area Of Applications Are</h2>
  <p class="lead">Lorem ipsum dolor sit amet, consectetuer adipiscing elit, sed diam nonummy nibh euismod tincidunt ut laoreet dolore magna aliquam erat volutpat. Ut wisi enim ad minim veniam, quis nostrud exerci tation ullamcorper.</p>
  <div class="app-cards">
    <article class="app-card">
      <svg viewBox="0 0 72 72"><g transform="rotate(-35 24 34)"><rect x="14" y="10" width="20" height="48" rx="10" fill="#0a9bd8"/><rect x="14" y="32" width="20" height="2" fill="#f4f4f4"/></g><g transform="rotate(-40 48 48)"><rect x="38" y="32" width="20" height="34" rx="10" fill="#0a9bd8"/><rect x="38" y="48" width="20" height="2" fill="#f4f4f4"/></g></svg>
      <h3>Pharmaceutical</h3>
      <p>Lorem ipsum dolor sit amet, consectetuer adipiscing elit, sed diam non...</p>
    </article>
    <article class="app-card is-active">
      <svg viewBox="0 0 72 72" fill="none" stroke="#fff" stroke-width="3"><path d="M36 34s-12-7-12-15a6 6 0 0112-2 6 6 0 0112 2c0 8-12 15-12 15z" fill="#fff"/><path d="M8 26v16c0 6 4 9 8 12l10 8h6V50l-10-10"/><path d="M64 26v16c0 6-4 9-8 12l-10 8h-6V50l10-10"/></svg>
      <h3>Therapeutic</h3>
      <p>Lorem ipsum dolor sit amet, consectetuer adipiscing elit, sed diam non...</p>
    </article>
    <article class="app-card">
      <svg viewBox="0 0 72 72" fill="none" stroke="#0a9bd8" stroke-width="2.5"><path d="M50 10l12 12M56 16l-8 8"/><rect x="24" y="20" width="12" height="36" transform="rotate(45 30 38)"/><path d="M22 50l-14 14M40 18l14 14M30 34l4 4M26 38l4 4M34 30l4 4"/></svg>
      <h3>Vaccination</h3>
      <p>Lorem ipsum dolor sit amet, consectetuer adipiscing elit, sed diam non...</p>
    </article>
  </div>
</section>

<section class="section about">
  <h2>About Antigen Preservation Bureau</h2>
  <div class="about-text">
    <p>Lorem ipsum dolor sit amet, consectetuer adipiscing elit, sed diam nonummy nibh euismod tincidunt ut laoreet dolore maa aliquam erat volutpat. Ut wisi enim ad minim veniam, quis nostrud exerci tation ullamcorper suscipit lobortis nisl ut aliquip ex ea.</p>
    <p>Lit, sed diam nonummy nibh euismod tincidunt ut laoreet dolore mana aliquam erat volutpat. Ut wisi enim ad minim veniam, quis nostrud exerci tation ullamcorper suscipit. nonummy nibh euismod tincidunt ut laoreet.</p>
  </div>
  <a class="btn btn-read" href="#">Read More</a>
  <div class="video" role="img" aria-label="Introductory video about Antigen Preservation Bureau">
    <div class="video-name">Antigen Preservation Bureau</div>
    <svg class="video-play" width="50" height="50" viewBox="0 0 50 50"><circle cx="25" cy="25" r="23" fill="rgba(0,0,0,.45)" stroke="#fff" stroke-width="2"/><path d="M20 15l15 10-15 10z" fill="#fff"/></svg>
  </div>
</section>

<section class="section news">
  <h2 class="section-title">Latest News</h2>
  <div class="news-cards">
    <article class="news-card">
      <div class="news-media" role="img" aria-label="Researcher in gloves working at a laboratory bench"><div class="date"><b>05</b><i>JAN '19</i></div></div>
      <h3>Lit, sed diam nonummy niby nib euismod tincidunt ut laoreet.</h3>
      <p>Lorem ipsum dolor sit amet nsectetuer adipiscing elit, sed diam nonummy nibh euismod tincidunt ut laoreet dolore maa aliquam erat volutpat.</p>
      <a class="more" href="#">Continue Reading →</a>
    </article>
    <article class="news-card">
      <div class="news-media" role="img" aria-label="Glass vaccine vial with a blue cap lying on its side"><div class="date"><b>05</b><i>JAN '19</i></div></div>
      <h3>Lit, sed diam nonummy niby nib euismod tincidunt ut laoreet.</h3>
      <p>Lorem ipsum dolor sit amet nsectetuer adipiscing elit, sed diam nonummy nibh euismod tincidunt ut laoreet dolore maa aliquam erat volutpat.</p>
      <a class="more" href="#">Continue Reading →</a>
    </article>
    <article class="news-card">
      <div class="news-media" role="img" aria-label="Gloved hand adjusting a bioprocess bag on lab equipment"><div class="date"><b>05</b><i>JAN '19</i></div></div>
      <h3>Lit, sed diam nonummy niby nib euismod tincidunt ut laoreet.</h3>
      <p>Lorem ipsum dolor sit amet nsectetuer adipiscing elit, sed diam nonummy nibh euismod tincidunt ut laoreet dolore maa aliquam erat volutpat.</p>
      <a class="more" href="#">Continue Reading →</a>
    </article>
  </div>
</section>

<section class="section licensing">
  <h2>Also offering some licensing opportunities for stabilizing technologies.</h2>
  <p class="lead">Lorem ipsum dolor sit amet, consectetuer adipiscing elit, sed diam nonummy nibh euismod tincidunt ut laoreet dolore magna aliquam erat volutpat. Ut wisi enim ad minim veniam, quis nostrud exerci tation ullamcorper.</p>
  <a class="btn btn-call" href="#"><svg width="20" height="20" viewBox="0 0 24 24" fill="none" stroke="#fff" stroke-width="2"><circle cx="12" cy="12" r="10"/><path d="M8.5 7.5l2 2-1 1.5a7 7 0 003.5 3.5l1.5-1 2 2-1.5 1.5c-3.5 0-8-4.5-8-8z" fill="#fff" stroke="none"/></svg>123.456.7890</a>
</section>

<footer class="section site-footer">
  <div class="footer-col links">
    <h4>Quick Links</h4>
    <ul><li>Home</li><li>About Us</li><li>Services</li><li>News</li><li>Contact Us</li></ul>
  </div>
  <div class="footer-col contacts">
    <h4>Contact Details</h4>
    <div class="contact-row"><svg width="14" height="18" viewBox="0 0 14 18"><path d="M7 0a7 7 0 017 7c0 5-7 11-7 11S0 12 0 7a7 7 0 017-7z" fill="#fff"/><circle cx="7" cy="7" r="2.5" fill="#333"/></svg><span>Antigen Preservation Bureau<br>Street Name, City<br>Name State Zipcode</span></div>
    <div class="contact-row"><svg width="18" height="18" viewBox="0 0 24 24" fill="none" stroke="#fff" stroke-width="2"><circle cx="12" cy="12" r="10"/><path d="M8.5 7.5l2 2-1 1.5a7 7 0 003.5 3.5l1.5-1 2 2-1.5 1.5c-3.5 0-8-4.5-8-8z" fill="#fff" stroke="none"/></svg><span>123.456.7890</span></div>
    <div class="contact-row"><svg width="18" height="14" viewBox="0 0 20 16" fill="none" stroke="#fff" stroke-width="1.8"><rect x="1" y="1" width="18" height="14"/><path d="M1 1l9 7 9-7"/></svg><span>inquiry@apb.com</span></div>
  </div>
  <div class="footer-col map-col">
    <h4>Location Map</h4>
    <div class="map" role="img" aria-label="Street map showing the office location"></div>
  </div>
  <div class="footer-col follow">
    <h4>Follow Us On</h4>
    <div class="socials"><span></span><span></span><span></span></div>
    <div class="footer-brand">Antigen Preservation Bureau</div>
  </div>
</footer>

<div class="section bottom-bar">
  <p class="copy">Copyright © 2019 Antigen Preservation Bureau. All Rights Reserved.</p>
  <p class="legal">Terms &amp; Conditions | Privacy Policy</p>
</div>

</body>
</html>
```